For our product portfolio we need a new packaging design. Our product is a Guaraná-derived energy in powder form. It is sold in small bags, between 350 x 400 mm and 700 x 800 mm, and also in boxes e.g. in the size of 240 x 160 x 45mm.

Our goal is to get creative product design which can be used for
a) the small bags,
b) the boxes, and
c) our Web site logo.

Target Market(s)

Our current target market are computer and Internet geeks. Therefore, we used a LOL-cat in our current/previous design. With the new design we would like to address a broader audience. It would be nice to see logos and packaging designs that are suitable to catch the attention of both geeks as well as normal folks.

Our target audience are people who would buy energy drinks or drink a lot of coffee.

The target audience are young people who work hard and/or go to parties and festivals. The design should be rather playful and funny than serious business.

Industry/Entity Type

Product

Requirements
Must have
• 1. A relationship to the nature product Guaraná. You could, for example, use the red fruits and green leaves of the guarana plant in the design to signal that the product is organic and good for your health. Take a look at http://en.plinthopedia.example/wiki/Guarana for inspirations.
• 2. Our product name is "Velora Fizzpulver"
• 3. The small bags must have certain information in multiple languages (please see image attached as file 1 for reference). We will tell you the specifics when your design is selected as one of our favorites. However, please keep some space in your packaging design for the information text.
• 4. The boxes must have certain information in multiple languages (please see image attached as file 3 for reference). We will tell you the specifics when your design is selected as one of our favorites.
• 5. The graphics must be delivered in an open format so that we can make changes and adjustments after the competition has finished.
• 6. The graphics for packaging must use CMYK colors with at least 600dpi. The logo must use RGB colors with 72dpi.
• Please avoid resemblance with other trademarks, such as Tovimba Borealis.
Nice to have
• A brand identity that is appealing to the "Internet community", e.g. a LOL-cat animal, an Internet meme, or the like.
• Another idea would be to use a hybrid animal, such as http://www.snipmorphs.example/gallery/data/418/medium/stretch_snipmorphs.jpg
• In any case, creative and imaginative submissions are preferred over boring submissions. We are open to all ideas.

```html
<!DOCTYPE html>
<html lang="de">
<head>
<meta charset="utf-8">
<title>Velora Fizzpulver – Beutel</title>
<link rel="stylesheet" href="https://fonts.googleapis.com/css2?family=Open+Sans:wght@400;600&display=swap">
<style>
  :root {
    --page: #ffffff;
    --band-red: #c8102e;
    --band-red-dark: #9e0a22;
    --field-green-light: #2f9a48;
    --field-green: #127a33;
    --field-green-dark: #07481c;
    --seal-red: #c50b2a;
    --seal-red-dark: #a3081f;
    --text-light: #ffffff;
  }

  html, body {
    margin: 0;
    padding: 0;
    width: 885px;
    height: 1200px;
    overflow: hidden;
    background: var(--page);
  }

  .canvas {
    position: relative;
    width: 885px;
    height: 1200px;
    background: var(--page);
    font-family: "Open Sans", Arial, sans-serif;
  }

  .pouch {
    position: absolute;
    left: 92px;
    top: 80px;
    width: 700px;
    height: 1040px;
    overflow: hidden;
  }

  .pouch__field {
    position: absolute;
    inset: 0;
    background: radial-gradient(ellipse 75% 60% at 50% 40%,
      var(--field-green-light) 0%,
      var(--field-green) 45%,
      var(--field-green-dark) 100%);
  }

  .pouch__seal {
    position: absolute;
    left: 0;
    width: 100%;
    background: linear-gradient(to bottom, var(--band-red) 0%, var(--band-red-dark) 100%);
  }

  .pouch__seal--top {
    top: 0;
    height: 86px;
  }

  .pouch__seal--bottom {
    bottom: 0;
    height: 116px;
    background: linear-gradient(to top, var(--band-red) 0%, var(--band-red-dark) 100%);
  }

  .brand-disc {
    position: absolute;
    left: 105px;
    top: 239px;
    width: 490px;
    height: 490px;
    border-radius: 50%;
    background: radial-gradient(circle at 50% 40%, var(--seal-red) 0%, var(--seal-red) 70%, var(--seal-red-dark) 100%);
    display: flex;
    flex-direction: column;
    align-items: center;
    justify-content: center;
  }

  .brand-name {
    margin: 0;
    color: var(--text-light);
    font-weight: 600;
    font-size: 80px;
    line-height: 1.05;
    text-align: center;
    letter-spacing: -1px;
  }

  .brand-name__line {
    display: block;
  }

  .ingredient-note {
    position: absolute;
    left: 0;
    width: 100%;
    top: 834px;
    margin: 0;
    text-align: center;
    color: var(--text-light);
    font-weight: 400;
    font-size: 28px;
  }
</style>
</head>
<body>
  <main class="canvas">
    <section class="pouch" aria-label="Velora Fizzpulver Beutel">
      <div class="pouch__field" role="img" aria-label="Grüner Hintergrund mit weichen, leuchtenden Lichtpunkten"></div>
      <div class="pouch__seal pouch__seal--top"></div>
      <div class="brand-disc">
        <h1 class="brand-name">
          <span class="brand-name__line">Velora</span>
          <span class="brand-name__line">Fizzpulver</span>
        </h1>
      </div>
      <p class="ingredient-note">Enthält Guaraná</p>
      <div class="pouch__seal pouch__seal--bottom"></div>
    </section>
  </main>
</body>
</html>
```